Cedar Hollow at Pine Basin Marketing Sign

I need a sign designed that will be 4'X8'. You designed another sign for me not too long ago - Fernridge at Harlow's Point. I need another sign similar in layout, but with the Cedar Hollow logo, tagline, rendering, colors, etc.

Attached is the logo, and rendering. Here are the other items I need to have on this sign:
Tagline - Life Outside The Lines
JOIN OUR WAITLIST TODAY!
Move-In Beginning Summer 2017
www.cedarhollowhomesx.com

```html
<!DOCTYPE html>
<html lang="en">
<head>
<meta charset="utf-8">
<title>Cedar Hollow at Pine Basin – Marketing Sign</title>
<link rel="stylesheet" href="https://fonts.googleapis.com/css2?family=Jost:wght@400;500;600&family=Great+Vibes&display=swap">
<style>
  :root {
    --backdrop: #2b2b2b;
    --sign-white: #ffffff;
    --teal: #1b9fb8;
    --teal-band: rgba(27, 159, 184, 0.85);
    --brand-blue: #2277a8;
    --panel-grey: #ececec;
    --text-grey: #555555;
    --render-sky: #b9c9e0;
    --render-tree: #8aa457;
    --render-ground: #9a8f93;
  }
  * { margin: 0; padding: 0; box-sizing: border-box; }
  html, body {
    width: 960px; height: 1200px; overflow: hidden;
    background: var(--backdrop);
  }
  .sign {
    position: absolute; left: 195px; top: 30px;
    width: 570px; height: 1140px;
    background: var(--sign-white);
    font-family: "Jost", "Futura", sans-serif;
  }
  .brand {
    position: absolute; top: 38px; left: 0; width: 100%;
    display: flex; flex-direction: column; align-items: center;
  }
  .brand-mark {
    width: 88px; height: 88px;
    border: 3px solid var(--brand-blue);
  }
  .brand-name {
    margin-top: 18px;
    font-size: 27px; font-weight: 500;
    color: var(--teal);
    text-align: center; line-height: 1.15;
    letter-spacing: 0.5px;
    width: 250px;
  }
  .rendering {
    position: absolute; top: 249px; left: 0;
    width: 570px; height: 422px;
    background:
      linear-gradient(to bottom, var(--render-sky) 0%, #d8dde6 30%, var(--render-tree) 55%, #b7a79a 75%, var(--render-ground) 100%);
  }
  .tagline-band {
    position: absolute; top: 589px; left: 0;
    width: 570px; height: 65px;
    background: var(--teal-band);
    display: flex; align-items: center; justify-content: center;
  }
  .tagline {
    font-family: "Great Vibes", cursive;
    font-size: 50px; color: #ffffff;
    line-height: 1;
  }
  .cta-lead {
    position: absolute; top: 716px; left: 0; width: 100%;
    text-align: center;
    font-size: 56px; font-weight: 500;
    color: var(--teal); line-height: 1;
  }
  .cta-main {
    position: absolute; top: 770px; left: 0; width: 100%;
    text-align: center;
    font-size: 128px; font-weight: 600;
    color: var(--brand-blue); line-height: 1;
    letter-spacing: -1px;
  }
  .move-in {
    position: absolute; top: 920px; left: 0;
    width: 570px; height: 126px;
    background: var(--panel-grey);
    display: flex; flex-direction: column; align-items: center; justify-content: center;
    color: var(--text-grey); line-height: 1.15;
  }
  .move-in-label { font-size: 44px; font-weight: 400; }
  .move-in-date { font-size: 44px; font-weight: 500; }
  .web-bar {
    position: absolute; top: 1074px; left: 0;
    width: 570px; height: 66px;
    background: var(--brand-blue);
    display: flex; align-items: center; justify-content: center; gap: 14px;
    color: #ffffff;
  }
  .web-icon { width: 28px; height: 28px; }
  .web-url { font-size: 29px; font-weight: 500; }
</style>
</head>
<body>
  <main class="sign">
    <header class="brand">
      <div class="brand-mark"></div>
      <div class="brand-name">Cedar Hollow at Pine Basin</div>
    </header>

    <div class="rendering" role="img" aria-label="Watercolor rendering of three-story apartment buildings among trees with a parking lot in front"></div>
    <div class="tagline-band">
      <span class="tagline">Life Outside The Lines</span>
    </div>

    <p class="cta-lead">JOIN OUR WAITLIST</p>
    <p class="cta-main">TODAY!</p>

    <section class="move-in">
      <span class="move-in-label">Move-In Beginning</span>
      <span class="move-in-date">Summer 2017</span>
    </section>

    <footer class="web-bar">
      <svg class="web-icon" viewBox="0 0 28 28" fill="none" stroke="#ffffff" stroke-width="2">
        <circle cx="14" cy="14" r="12"/>
        <ellipse cx="14" cy="14" rx="5.5" ry="12"/>
        <line x1="2" y1="14" x2="26" y2="14"/>
        <line x1="4" y1="8" x2="24" y2="8"/>
        <line x1="4" y1="20" x2="24" y2="20"/>
      </svg>
      <span class="web-url">www.cedarhollowhomesx.com</span>
    </footer>
  </main>
</body>
</html>
```